International Consultancy Needs Slick Professional Presentation Graphic

Varnolt are an international engineering and advisory consultancy servicing the mining industry with a mix of Technology (Software), Services (consulting) and Systems (work structures).

We need a slick presentation graphic for use in presentation slides, whitepapers. I have attached a basic pic of the information we want to convey. Flat or 3D no preference, colouring no preference. Don't have to be circles, that was just easiest to draft up initially.

Industry/Entity Type

Mining

```html
<!DOCTYPE html>
<html lang="en">
<head>
<meta charset="utf-8">
<title>Varnolt — Services, Systems, Technology</title>
<link rel="stylesheet" href="https://fonts.googleapis.com/css2?family=Noto+Sans+Mono:wght@400;700&display=swap">
<style>
  :root {
    --ink: #111111;
    --accent: #9b1c22;
    --paper: #ffffff;
  }
  html, body {
    margin: 0;
    padding: 0;
    width: 1200px;
    height: 927px;
    overflow: hidden;
    background: var(--paper);
  }
  .pillar-diagram {
    display: block;
    width: 1200px;
    height: 927px;
  }
  .pillar-frame {
    fill: none;
    stroke: var(--accent);
    stroke-width: 7;
    stroke-linejoin: miter;
  }
  .pillar-title {
    font-family: "Noto Sans Mono", monospace;
    font-weight: 700;
    font-size: 64px;
    fill: var(--ink);
  }
  .pillar-initial {
    fill: var(--accent);
  }
  .link-label {
    font-family: "Noto Sans Mono", monospace;
    font-weight: 400;
    font-size: 22px;
    fill: var(--ink);
  }
</style>
</head>
<body>
<svg class="pillar-diagram" viewBox="0 0 1200 927" xmlns="http://www.w3.org/2000/svg" role="img" aria-label="Services, Systems and Technology linked by organisation design, user interface engineering and system interface engineering">
  <!-- Services pillar -->
  <g class="pillar pillar--services">
    <polyline class="pillar-frame" points="767,176 615,176 523,306 583,372 896,372"/>
    <text class="pillar-title" x="585" y="327"><tspan class="pillar-initial">S</tspan>ervices</text>
  </g>

  <!-- Systems pillar -->
  <g class="pillar pillar--systems">
    <polyline class="pillar-frame" points="288,402 424,402 483,467 390,599 143,599"/>
    <text class="pillar-title" x="168" y="492"><tspan class="pillar-initial">S</tspan>ystems</text>
  </g>

  <!-- Technology pillar -->
  <g class="pillar pillar--technology">
    <polyline class="pillar-frame" points="845,521 632,521 540,654 599,718 993,718"/>
    <text class="pillar-title" x="588" y="682"><tspan class="pillar-initial">T</tspan>echnology</text>
  </g>

  <!-- Links between pillars -->
  <g class="link link--organisation-design">
    <text class="link-label" x="342" y="362">Organisation</text>
    <text class="link-label" x="459" y="406">Design</text>
  </g>
  <g class="link link--user-interface">
    <text class="link-label" x="711" y="411">User</text>
    <text class="link-label" x="676" y="453">Interface</text>
    <text class="link-label" x="665" y="498">Engineering</text>
  </g>
  <g class="link link--system-interface">
    <text class="link-label" x="489" y="535">System</text>
    <text class="link-label" x="438" y="586">Interface</text>
    <text class="link-label" x="375" y="639">Engineering</text>
  </g>
</svg>
</body>
</html>
```